Book Cover Design Project

I would like a book cover designed for a book entitled: Bright Days Ahead: Finding the Right Tooth Artist
The target audience is those patients interested in cosmetic dentistry. Generally those would be people over 45, with above average income, but the cover should have more universal appeal.
The book was written by
Marcus T. Whitfield, DDS, FSFOC
Fellow in the Society of Family Oral Care
(that's me)
The book will be distributed as an ebook for free to patients and potential patients interested in cosmetic dentistry.

```html
<!DOCTYPE html>
<html lang="en">
<head>
<meta charset="utf-8">
<title>Bright Days Ahead: Finding the Right Tooth Artist</title>
<link href="https://fonts.googleapis.com/css2?family=Alegreya+Sans+SC:wght@800&family=PT+Sans:wght@400&display=swap" rel="stylesheet">
<style>
  :root {
    --page-bg: #232323;
    --cover-blue: #0a7fca;
    --cover-green: #0e9640;
    --title-green: #0e8f3d;
    --white: #ffffff;
    --skin-light: #e7b295;
    --skin-mid: #c98466;
    --skin-deep: #b0604d;
  }
  * { margin: 0; padding: 0; box-sizing: border-box; }
  html, body {
    width: 1200px;
    height: 960px;
    overflow: hidden;
    background: var(--page-bg);
  }
  .stage {
    width: 1200px;
    height: 960px;
    display: flex;
    align-items: center;
    justify-content: center;
  }
  .book-cover {
    position: relative;
    width: 695px;
    height: 900px;
    background: var(--cover-blue);
    overflow: hidden;
  }
  .cover-art {
    position: absolute;
    inset: 0;
    width: 100%;
    height: 100%;
  }
  .title-plate {
    position: absolute;
    left: 78px;
    top: 41px;
    width: 539px;
    height: 125px;
    background: var(--white);
    border-radius: 26px;
    display: flex;
    flex-direction: column;
    align-items: center;
    justify-content: center;
    gap: 2px;
  }
  .book-title {
    font-family: "Alegreya Sans SC", sans-serif;
    font-weight: 800;
    font-size: 56px;
    line-height: 1;
    color: var(--title-green);
    letter-spacing: 0.5px;
  }
  .book-subtitle {
    font-family: "PT Sans", sans-serif;
    font-weight: 400;
    font-size: 26px;
    line-height: 1.1;
    color: var(--title-green);
    letter-spacing: 1px;
  }
  .author-block {
    position: absolute;
    left: 0;
    right: 0;
    top: 842px;
    text-align: center;
    font-family: "PT Sans", sans-serif;
    font-size: 13px;
    line-height: 1.55;
    color: var(--white);
  }
</style>
</head>
<body>
  <main class="stage">
    <section class="book-cover">
      <svg class="cover-art" viewBox="0 0 612 792" preserveAspectRatio="none" aria-hidden="false">
        <defs>
          <radialGradient id="smile-tones" cx="50%" cy="55%" r="60%">
            <stop offset="0%" stop-color="var(--skin-mid)"/>
            <stop offset="55%" stop-color="var(--skin-light)"/>
            <stop offset="100%" stop-color="var(--skin-deep)"/>
          </radialGradient>
        </defs>
        <path class="green-wave" d="M0,469 C60,600 200,680 340,700 C460,718 570,730 612,775 L612,792 L0,792 Z" fill="var(--cover-green)"/>
        <path class="wave-edge" d="M0,469 C60,600 200,680 340,700 C460,718 570,730 612,775" fill="none" stroke="var(--white)" stroke-width="12"/>
        <g class="heart-photo" role="img" aria-label="Close-up photograph of a smiling mouth with white teeth, framed in a heart">
          <path d="M306,275 C280,200 200,180 140,195 C80,210 60,270 70,330 C85,420 200,500 306,632 C410,500 530,420 545,330 C555,270 535,210 475,195 C415,180 335,200 306,275 Z"
                fill="url(#smile-tones)" stroke="var(--white)" stroke-width="14" stroke-linejoin="round"/>
        </g>
      </svg>

      <header class="title-plate">
        <h1 class="book-title">Bright Days Ahead</h1>
        <p class="book-subtitle">Finding the Right Tooth Artist</p>
      </header>

      <footer class="author-block">
        <p class="author-name">Marcus T. Whitfield, DDS, FSFOC</p>
        <p class="author-credential">Fellow in the Society of Family Oral Care</p>
      </footer>
    </section>
  </main>
</body>
</html>
```